Pharmaceutical Manufacturing Services Advertisement

We need a new full page advertisement designed for publication in international magazines. We are a custom pharmaceutical manufacturing company and we help biotechnology companies scale up their drug development for clinical trials. The products we help manufacture are therapeutics for global healthcare problems.

Target Market(s)

Verott Bio is a privately owned contract development manufacturing organisation (CDMO) headquartered in Darra, QLD, Australia.

Our mission is to is to be a global leader in development and in the provision of contract manufacturing for active pharmaceutical ingredient processes.

Why we do what we Do:

To help advance Biotechnology Companies so that they can deliver innovative therapeutics
~ enabling patients to live longer, healthier and happier lives
~ which solves worldwide health problems

Verott Bio’s role is to develop, implement and scale up the production to deliver biologic medicines for patients in partnership with the biotechnology companies.

Industry/Entity Type

Biotechnology

Font styles to use
Sans Serif

Colors

Designer to choose colors to be used in the design.

Requirements
Must have
• Please see the script on the Word document. There are 4 optional Header Taglines. Additional ideas for multiple designs for the taglines welcomed.
• However preference is for either of the first two:
• 1. Building your vision for better healthcare
• 2. Bridging your vision for better healthcare
• File Specs:
• • All artwork should be submitted as high-resolution (300 min. dpi), press-ready PDF files
• • CMYK color only
• • Full page 8.25” x 10.812”; 209.55 x 274.62 mm
• • Live Area for all sizes: 0.25” (6.35 mm) inside the trim
• • Bleed Area for all sizes: Extends 0.125” (3.175 mm) from trim
Nice to have
• Modern Science look to inspire biotechnology companies to work with us.
• Search for images to use by keyword "recombinant dna"

```html
<!DOCTYPE html>
<html lang="en">
<head>
<meta charset="utf-8">
<title>Verott Bio – Building Your Vision for Better Healthcare</title>
<link href="https://fonts.googleapis.com/css2?family=Montserrat:wght@300;400;700;800&family=Arimo:wght@400;700&display=swap" rel="stylesheet">
<style>
  :root {
    --navy: #0f3a5c;
    --lime: #a4bd2b;
    --white: #ffffff;
    --backdrop: #0d3a58;
    --photo-light: #e4edf3;
    --photo-mid: #b8cddd;
    --photo-dark: #7f9cb3;
  }
  * { box-sizing: border-box; margin: 0; padding: 0; }
  html, body { width: 1200px; height: 1180px; overflow: hidden; }
  body { background: var(--backdrop); font-family: "Arimo", Arial, sans-serif; }

  .ad-page {
    position: absolute; left: 216px; top: 30px;
    width: 767px; height: 1120px;
    background: var(--white); overflow: hidden;
  }
  .hero-art { position: absolute; left: 0; top: 0; width: 767px; height: 760px; }

  .headline {
    position: absolute; left: 30px; top: 18px;
    font-family: "Montserrat", Arial, sans-serif; color: var(--navy);
    line-height: 1.04; text-transform: uppercase;
  }
  .headline-light { display: block; font-weight: 300; font-size: 58px; letter-spacing: 1px; }
  .headline-accent { display: block; font-weight: 800; font-size: 58px; color: var(--lime); letter-spacing: 1px; }
  .headline-strong { display: block; font-weight: 800; font-size: 46px; letter-spacing: 0.5px; }

  .tagline-band {
    position: absolute; left: 0; top: 281px; width: 400px; height: 72px;
    background: var(--lime); color: var(--white);
    font-weight: 700; font-size: 17px; line-height: 1.3;
    padding: 13px 0 0 30px;
  }

  .intro-copy {
    position: absolute; left: 30px; top: 392px; width: 268px;
    color: var(--white); font-size: 14px; line-height: 1.5;
  }

  .offer-box {
    position: absolute; top: 762px; height: 222px;
    border-right: 2px solid var(--lime); border-bottom: 2px solid var(--lime);
  }
  .offer-box.services { left: 0; width: 353px; padding: 20px 0 0 34px; }
  .offer-box.products { left: 388px; width: 379px; border-right: none; border-left: 2px solid var(--lime); padding: 20px 0 0 34px; }
  .offer-title { font-size: 25px; font-weight: 700; color: var(--navy); margin-bottom: 10px; }
  .offer-list { list-style: none; }
  .offer-list li {
    position: relative; padding-left: 16px;
    font-size: 18px; font-weight: 700; color: var(--navy); line-height: 1.42;
  }
  .offer-list li::before {
    content: ""; position: absolute; left: 0; top: 9px;
    width: 7px; height: 7px; border-radius: 50%; background: var(--lime);
  }
  .products .offer-list li { font-size: 17px; }

  .brand-block { position: absolute; left: 30px; top: 1040px; }
  .brand-name {
    font-family: "Montserrat", Arial, sans-serif; font-weight: 400;
    font-size: 36px; color: var(--navy); letter-spacing: 0.5px; line-height: 1;
  }
  .brand-descriptor {
    margin-top: 8px; font-size: 12px; color: var(--navy); letter-spacing: 0.3px;
  }
  .contact-line {
    position: absolute; left: 318px; top: 1050px;
    font-size: 15px; color: var(--navy); line-height: 1.55;
  }
</style>
</head>
<body>
  <main class="ad-page">
    <svg class="hero-art" viewBox="0 0 767 760">
      <defs>
        <linearGradient id="photoTone" x1="0" y1="0" x2="1" y2="1">
          <stop offset="0" stop-color="#e4edf3"/>
          <stop offset="0.55" stop-color="#b8cddd"/>
          <stop offset="1" stop-color="#7f9cb3"/>
        </linearGradient>
      </defs>
      <rect class="intro-panel" x="0" y="368" width="420" height="340" fill="#0f3a5c"/>
      <g role="img" aria-label="Photo of a scientist in safety glasses and blue gloves examining a test tube in a laboratory">
        <rect x="440" y="0" width="327" height="300" fill="url(#photoTone)"/>
        <circle cx="604" cy="470" r="256" fill="url(#photoTone)"/>
      </g>
      <circle class="photo-ring" cx="604" cy="470" r="272" fill="none" stroke="#0f3a5c" stroke-width="34"/>
    </svg>

    <h1 class="headline">
      <span class="headline-light">Building your</span>
      <span class="headline-light">vision for</span>
      <span class="headline-accent">Better</span>
      <span class="headline-strong">Healthcare</span>
    </h1>

    <p class="tagline-band">Your Partner in Early Phase<br>Clinical Biomanufacturing</p>

    <p class="intro-copy">We have been serving the pharmaceutical, biotechnology and veterinary industry for over 20 years so you can create innovative medicines for worldwide health problems. Get your therapeutics to the patient faster with cost-effective manufacturing for your GMP clinical trial material. We offer rapid technology transfer, scale-up development and manufacturing of microbial cell-derived proteins at up to 500L scale. We prepare your active pharmaceutical ingredient (API) products to a world class standard ready for clinical development.</p>

    <section class="offer-box services">
      <h2 class="offer-title">Services:</h2>
      <ul class="offer-list">
        <li>Bacterial / Yeast Fermentation</li>
        <li>Cell Banking</li>
        <li>Process Development/Scale-up</li>
        <li>cGMP Manufacture of<br>biopharmaceutical APIs</li>
        <li>Stability Testing</li>
      </ul>
    </section>

    <section class="offer-box products">
      <h2 class="offer-title">Products:</h2>
      <ul class="offer-list">
        <li>Recombinant proteins</li>
        <li>Live Biotherapeutics</li>
        <li>Bacterial vaccines</li>
        <li>Plasmid DNA</li>
      </ul>
    </section>

    <footer>
      <div class="brand-block">
        <div class="brand-name">VEROTT BIO</div>
        <div class="brand-descriptor">BIOPHARMACEUTICAL MANUFACTURING</div>
      </div>
      <p class="contact-line">Phone: +61(7)3000 4812 Email enquiries@verottbio.com.au<br>Visit: www.verottbio.com.au</p>
    </footer>
  </main>
</body>
</html>
```